Exclusive Pet groomer Post Card

We need a design for a direct mailing postcard. We want to include images of some of dogs and cats done the list of our services and the benefits of our company.

I like something like: Does your pet look like any of these or is a similar breed?

If your answer is yes, then it deserves the best groomer in town

any ideas are welcome!

URGENT Mailing Postcard needed!

Elegant, modern and clean sophisticated card that has images of the dogs and cats provided. I will use the original images from the image bank once the project is approved. As a designer you just need to create the layout for this and the organization!

Thanks

Target Market(s)

High Income professionals that will pay for premium services for their pets.

Industry/Entity Type

Pet

Requirements
Must have
• A full color double sided postcard. 5.5 x 8.5 in postcard. (I want to have all pics uploaded. I used some sample images from stock photo but once approved I will purchase the images at the respective site). Must have space to place recipient address and space for NPDS stamp. ( is a postcard to be mailed!)

I would like to have the following text in the post card:

Enhance the beauty of your pets
Pamper your best friend
Give to your dog or cat the stylish treatment it deserves

One of the top groomers in town
Experienced in dogs and cats
Clean individual pet grooming stations (Sanitation and Sterilization)
Services:
Full service grooming* services for dogs and cats include:
Day Spa, High Fashion Haircuts, hair trimming, nail clipping and “Petticures”
Bathing, gentle ear Cleaning, sanitary trim, Brushing, Fluff Drying and Dematting
* Regular grooming ensures happier and healthier pets

Fur Harbor Trim
2716 NE 147th Street, North Miami, Florida 33181
T. 305-647-3918
www.furharbortrim.example
Nice to have
• Logo as in the website

```html
<!DOCTYPE html>
<html lang="en">
<head>
<meta charset="utf-8">
<title>Fur Harbor Trim – Postcard</title>
<link href="https://fonts.googleapis.com/css2?family=Quicksand:wght@400;500;600;700&display=swap" rel="stylesheet">
<style>
:root{
  --coral:#f26d62;
  --coral-deep:#e85a4f;
  --blush:#f9b3a9;
  --teal:#3fb3a8;
  --ink:#3a3a3a;
  --paper:#ffffff;
  --page:#f2f2f2;
}
*{box-sizing:border-box;margin:0;padding:0}
html,body{width:851px;height:1200px;overflow:hidden;background:var(--page)}
body{position:relative;font-family:'Quicksand',sans-serif;color:var(--ink)}
.card{position:absolute;left:51px;width:751px;overflow:hidden;box-shadow:0 2px 8px rgba(0,0,0,.18)}
.card--front{top:14px;height:552px;background:var(--paper)}
.card--back{top:603px;height:580px;background:var(--coral)}

.headline{position:absolute;left:30px;top:30px;width:120px;font-size:17px;font-weight:600;line-height:1.3;color:var(--ink)}
.stamp-box{position:absolute;left:622px;top:28px;width:105px;height:92px;border:1.5px solid #bbb}

.pet{position:absolute;width:100px;height:100px;border-radius:50%;border:3px solid var(--paper);box-shadow:0 0 0 3px var(--teal)}
.pet:nth-child(odd){box-shadow:0 0 0 3px var(--coral)}

.front-band{position:absolute;left:0;top:0}
.tagline{position:absolute;left:40px;top:478px;width:420px;font-size:19px;font-weight:500;color:var(--paper);line-height:1.3}

.bubble{position:absolute;border-radius:50%;background:var(--blush);display:flex;align-items:center;justify-content:center;text-align:center;font-size:13px;font-weight:600;line-height:1.25;padding:14px;color:var(--ink)}
.bubble--large{font-size:15px}
.tool{position:absolute;width:34px;height:34px;border-radius:50%;background:var(--paper);border:2px solid var(--ink)}

.art{position:absolute}
.art--cat{left:34px;top:300px;width:86px;height:140px;border-radius:40px;background:linear-gradient(#2b2b2b,#444)}
.art--dog{left:265px;top:232px;width:165px;height:210px;border-radius:70px 70px 50px 50px;background:linear-gradient(#2b2b2b 0%,#f4f4f4 55%,#e23a6d 100%)}

.services{position:absolute;left:34px;top:448px;width:470px;font-size:10.5px;line-height:1.45;color:var(--paper);font-weight:500}
.services strong{font-weight:700}

.contact{position:absolute;right:28px;top:498px;text-align:right;font-size:10px;line-height:1.4;color:var(--paper)}
.contact .brand{font-size:12px;font-weight:600}
</style>
</head>
<body>

<section class="card card--front">
  <p class="headline">Does your pet look like any of these or is a similar breed?</p>
  <div class="stamp-box" aria-label="Postage area"></div>

  <div class="pets">
    <div class="pet" style="left:232px;top:28px;background:linear-gradient(#d6b08a,#a57a52)" role="img" aria-label="Photo of a poodle-type dog"></div>
    <div class="pet" style="left:345px;top:28px;background:linear-gradient(#f1ede6,#cfc6b8)" role="img" aria-label="Photo of a white cat"></div>
    <div class="pet" style="left:458px;top:28px;background:linear-gradient(#eeeeee,#c9c9c9)" role="img" aria-label="Photo of a white poodle"></div>
    <div class="pet" style="left:119px;top:136px;background:linear-gradient(#c79a6a,#7b5736)" role="img" aria-label="Photo of a small long-haired dog"></div>
    <div class="pet" style="left:232px;top:136px;background:linear-gradient(#9a8f86,#5b524c)" role="img" aria-label="Photo of a schnauzer"></div>
    <div class="pet" style="left:345px;top:136px;background:linear-gradient(#f5f2ec,#d9d1c4)" role="img" aria-label="Photo of a fluffy white dog"></div>
    <div class="pet" style="left:458px;top:136px;background:linear-gradient(#444,#111)" role="img" aria-label="Photo of a black poodle"></div>
    <div class="pet" style="left:119px;top:244px;background:linear-gradient(#e6dccd,#b9a78e)" role="img" aria-label="Photo of a Maltese"></div>
    <div class="pet" style="left:232px;top:244px;background:linear-gradient(#d7a874,#94673d)" role="img" aria-label="Photo of a spaniel"></div>
    <div class="pet" style="left:345px;top:244px;background:linear-gradient(#ede6da,#c5b59c)" role="img" aria-label="Photo of a Persian cat"></div>
    <div class="pet" style="left:458px;top:244px;background:linear-gradient(#b98a5c,#6e4b2c)" role="img" aria-label="Photo of a terrier"></div>
    <div class="pet" style="left:119px;top:352px;background:linear-gradient(#f2efe9,#cdc4b6)" role="img" aria-label="Photo of a bichon"></div>
    <div class="pet" style="left:232px;top:352px;background:linear-gradient(#c9a37a,#8c6845)" role="img" aria-label="Photo of a long-haired dog"></div>
    <div class="pet" style="left:345px;top:352px;background:linear-gradient(#a7704a,#5e3a22)" role="img" aria-label="Photo of a spaniel puppy"></div>
    <div class="pet" style="left:458px;top:352px;background:linear-gradient(#d9c2a5,#9b7f5c)" role="img" aria-label="Photo of a small shaggy dog"></div>
  </div>

  <svg class="front-band" width="751" height="552" viewBox="0 0 751 552" aria-hidden="true">
    <polygon points="0,448 751,505 751,552 0,552" fill="var(--coral)"/>
  </svg>
  <p class="tagline">If your answer is yes, then it deserves the best groomer in town...</p>
</section>

<section class="card card--back">
  <div class="bubble" style="left:48px;top:37px;width:124px;height:124px">One of the top groomers in town</div>
  <div class="bubble" style="left:205px;top:84px;width:110px;height:110px">Enhance the beauty of your pets</div>
  <div class="bubble" style="left:361px;top:50px;width:110px;height:110px">Experienced in dogs and cats</div>
  <div class="bubble" style="left:514px;top:81px;width:116px;height:116px">Give to your dog or cat the stylish treatment it deserves</div>
  <div class="bubble" style="left:634px;top:54px;width:90px;height:90px">Pamper your best friend</div>
  <div class="bubble bubble--large" style="left:587px;top:247px;width:140px;height:140px">Clean individual pet grooming stations (Sanitation and Sterilization)</div>

  <div class="tool" style="left:44px;top:30px" role="img" aria-label="Scissors icon"></div>
  <div class="tool" style="left:244px;top:176px" role="img" aria-label="Brush icon"></div>
  <div class="tool" style="left:398px;top:34px" role="img" aria-label="Comb icon"></div>
  <div class="tool" style="left:556px;top:60px" role="img" aria-label="Grooming clipper icon"></div>
  <div class="tool" style="left:658px;top:36px" role="img" aria-label="Hair dryer icon"></div>

  <div class="art art--cat" role="img" aria-label="Illustration of a black cat"></div>
  <div class="art art--dog" role="img" aria-label="Illustration of a black and white dog with a pink bow"></div>

  <div class="services">
    <strong>Services:</strong><br>
    Full service grooming* services for dogs and cats include:<br>
    Day Spa, High Fashion Haircuts, hair trimming, nail clipping and “Petticures”<br>
    Bathing, gentle ear Cleaning, sanitary trim, Brushing, Fluff Drying and Dematting<br>
    * Regular grooming ensures happier and healthier pets
  </div>

  <div class="contact">
    <div class="brand">Fur Harbor Trim</div>
    2716 NE 147th Street, North Miami, Florida 33181<br>
    T. 305-647-3918<br>
    www.furharbortrim.example
  </div>
</section>

</body>
</html>
```